Thai Restruant Business Card Design

A Business card design for a Thai and Laos take away restaurant.

We are a highly respectable take away restaurant in a small shopping center.

The design must have a Papaya Tree and Thai Palace.

The final design should communicate, innovation, fun and delicious food.

Industry/Entity Type

Restaurant

Contact Information for Business Card

Mango Hearth, Thai & Lao Food, Shop 4. 17 Elmsworth Lane. Fairbrook N.S.W 2199, Tel. 02-96417725, Open 7 Days From 9.00am To 7.00pm

```html
<!DOCTYPE html>
<html lang="en">
<head>
<meta charset="utf-8">
<title>Mango Hearth – Business Card</title>
<link rel="stylesheet" href="https://fonts.googleapis.com/css2?family=Open+Sans:wght@400&display=swap">
<style>
  :root {
    --backdrop: #8a7e72;
    --card-paper: #f7f6f2;
    --palace-light: #ece8de;
    --palace-gold: #d9c9a3;
    --palace-green: #b9c2b0;
    --band-black: #0d0d0d;
    --leaf-dark: #2f5a2a;
    --leaf-mid: #5f8f3e;
    --papaya-orange: #e99a2c;
    --sky-blue: #b9d3e6;
    --brand-green: #3f7a34;
    --ink: #1c1c1c;
  }
  * { margin: 0; padding: 0; box-sizing: border-box; }
  html, body {
    width: 1200px;
    height: 707px;
    overflow: hidden;
    background: var(--backdrop);
    font-family: "Open Sans", Arial, sans-serif;
  }
  .business-card {
    position: absolute;
    left: 105px;
    top: 53px;
    width: 990px;
    height: 600px;
    background: var(--card-paper);
    overflow: hidden;
    box-shadow: 0 10px 28px rgba(0,0,0,0.28);
  }
  .card-art {
    position: absolute;
    inset: 0;
    width: 100%;
    height: 100%;
  }
  .card-text { position: absolute; line-height: 1; white-space: nowrap; }
  .brand-name {
    left: 38px; top: 58px;
    font-size: 80px;
    color: var(--brand-green);
    letter-spacing: 2px;
  }
  .brand-tagline {
    left: 146px; top: 162px;
    font-size: 46px;
    color: var(--brand-green);
    letter-spacing: 1px;
  }
  .address-line {
    font-size: 40px;
    color: var(--ink);
    letter-spacing: 1px;
  }
  .address-street { left: 104px; top: 270px; }
  .address-suburb { left: 86px; top: 322px; }
  .phone-line {
    left: 86px; top: 382px;
    font-size: 48px;
    color: var(--ink);
    letter-spacing: 1px;
  }
  .hours-line {
    left: 0; width: 640px;
    text-align: center;
    font-size: 33px;
    color: var(--ink);
  }
  .hours-days { top: 466px; }
  .hours-times { top: 510px; }
</style>
</head>
<body>
  <section class="business-card">
    <svg class="card-art" viewBox="0 0 578 350" preserveAspectRatio="none">
      <defs>
        <linearGradient id="palaceWash" x1="0" y1="0" x2="1" y2="1">
          <stop offset="0" stop-color="var(--palace-green)"/>
          <stop offset="0.35" stop-color="var(--palace-light)"/>
          <stop offset="0.65" stop-color="var(--palace-gold)"/>
          <stop offset="1" stop-color="var(--palace-light)"/>
        </linearGradient>
        <linearGradient id="papayaTree" x1="0" y1="0" x2="1" y2="1">
          <stop offset="0" stop-color="var(--sky-blue)"/>
          <stop offset="0.3" stop-color="var(--leaf-mid)"/>
          <stop offset="0.6" stop-color="var(--papaya-orange)"/>
          <stop offset="0.85" stop-color="var(--leaf-dark)"/>
          <stop offset="1" stop-color="var(--papaya-orange)"/>
        </linearGradient>
      </defs>
      <rect class="palace-scene" x="0" y="0" width="578" height="350" fill="url(#palaceWash)" opacity="0.55" role="img" aria-label="Faded photograph of a Thai palace with golden roofs and trees"/>
      <polygon class="papaya-tree" points="540,0 578,0 578,350 320,350" fill="url(#papayaTree)" role="img" aria-label="Illustration of a papaya tree with leaves and clusters of ripe papayas"/>
      <polygon class="black-band" points="360,0 540,0 320,350 305,350 478,92" fill="var(--band-black)"/>
    </svg>

    <div class="card-text brand-name">Mango Hearth</div>
    <div class="card-text brand-tagline">Thai &amp; Lao Food</div>
    <div class="card-text address-line address-street">Shop 4. 17 Elmsworth Lane.</div>
    <div class="card-text address-line address-suburb">Fairbrook N.S.W 2199</div>
    <div class="card-text phone-line">Tel. 02-96417725</div>
    <div class="card-text hours-line hours-days">Open 7 Days</div>
    <div class="card-text hours-line hours-times">From 9.00am To 7.00pm</div>
  </section>
</body>
</html>
```